Kito Rise and Glow Dance Fitness-KRGDF

Catchy POSTER .
The poster must attract both eyes of all ages looking for fitness,Ritmoflex to have fun, professional dance training and Yoga.

Target Market(s)

Dancers and Non Dancers

Industry/Entity Type

Training

Requirements
Must have
• Kito Dance Ensemble
Presents
KITO RISE AND GLOW DANCE FITNESS

African Dance
Modern/Samtidsdans,
Yoga
Ritmoflex
Hip Hop
Massage and repertoire classes.

Venue:Vetlefjord Kulturhus
Call 47351208 to register/TEXT
kitoarts@kitomail.example
www.kitoarts-example.org
Nice to have
• OG creativity...think outside the box
Should not have
• Please NO cartoon charectors!!! or BALLET DANCING LIONS!!!

```html
<!DOCTYPE html>
<html lang="en">
<head>
<meta charset="utf-8">
<title>Kito Dance Ensemble – Rise and Glow Dance Fitness</title>
<link rel="stylesheet" href="https://fonts.googleapis.com/css2?family=Passion+One:wght@700&family=Russo+One&family=Oswald:wght@600&display=swap">
<style>
  :root {
    --paper: #f3f4f5;
    --paper-shade: #dfe3e6;
    --frame: #59636b;
    --pink: #e0207a;
    --pink-deep: #b8125f;
    --pink-light: #f06aa8;
    --gold: #f2b418;
    --gold-light: #ffd65a;
    --ink: #2b2f33;
    --white: #ffffff;
    --glow-blue: #8fd3f4;
    --glow-green: #9be25c;
  }
  * { margin: 0; padding: 0; box-sizing: border-box; }
  html, body { width: 800px; height: 1200px; overflow: hidden; background: var(--white); }
  .poster {
    position: relative;
    width: 800px;
    height: 1200px;
    background: var(--white);
    overflow: hidden;
  }
  .card {
    position: absolute;
    left: 40px; top: 0;
    width: 720px; height: 1170px;
    background: radial-gradient(circle at 50% 35%, var(--white) 0%, var(--paper) 55%, var(--paper-shade) 100%);
    border: 4px solid var(--frame);
    border-top: none;
    box-shadow: 4px 6px 10px rgba(0,0,0,0.25);
    overflow: hidden;
  }
  .card p, .card h1, .card h2, .card span { white-space: nowrap; }
  .dancer-photo {
    position: absolute;
    left: 80px; top: 10px;
    width: 560px; height: 720px;
    background:
      radial-gradient(ellipse 45% 30% at 30% 55%, rgba(155,226,92,0.55), transparent 70%),
      radial-gradient(ellipse 55% 25% at 70% 55%, rgba(143,211,244,0.75), transparent 70%),
      radial-gradient(ellipse 28% 45% at 52% 40%, rgba(120,150,80,0.55), transparent 75%),
      radial-gradient(ellipse 22% 30% at 50% 75%, rgba(70,100,150,0.45), transparent 75%);
  }
  .brand-name {
    position: absolute;
    left: 0; width: 720px; top: 410px;
    text-align: center;
    font-family: "Passion One", "Arial Black", sans-serif;
    font-weight: 700;
    font-size: 170px;
    line-height: 1;
    letter-spacing: 2px;
    color: var(--pink);
    text-shadow: 2px 3px 0 rgba(255,255,255,0.7);
  }
  .ensemble {
    position: absolute;
    left: 0; width: 720px; top: 568px;
    text-align: center;
    font-family: "Passion One", "Arial Black", sans-serif;
    font-size: 66px;
    line-height: 1;
    color: var(--pink);
    text-shadow: 2px 2px 0 rgba(255,255,255,0.7);
  }
  .presents-band {
    position: absolute;
    left: 300px; top: 648px;
    width: 380px; height: 62px;
    background: linear-gradient(180deg, var(--gold-light), var(--gold));
    transform: skewX(-10deg);
    display: flex; align-items: center; justify-content: center;
  }
  .presents-band span {
    transform: skewX(10deg);
    font-family: "Russo One", sans-serif;
    font-size: 46px;
    letter-spacing: 6px;
    color: var(--white);
    text-shadow: 1px 2px 2px rgba(0,0,0,0.35);
  }
  .title-band {
    position: absolute;
    left: 60px; top: 708px;
    width: 630px; height: 54px;
    background: linear-gradient(180deg, var(--pink-light), var(--pink));
    display: flex; align-items: center; justify-content: center;
    font-family: "Russo One", sans-serif;
    font-weight: 400;
    font-size: 26px;
    letter-spacing: 1px;
    color: var(--white);
  }
  .class-list {
    position: absolute;
    left: 10px; top: 782px;
    width: 700px; height: 38px;
    background: linear-gradient(90deg, transparent, rgba(242,180,24,0.85) 6%, rgba(242,180,24,0.85) 94%, transparent);
    display: flex; align-items: center; justify-content: center; gap: 14px;
    font-family: "Russo One", sans-serif;
    font-size: 16px;
    color: var(--ink);
  }
  .class-list .accent { color: var(--pink-deep); }
  .massage-box {
    position: absolute;
    left: 70px; top: 845px;
    width: 600px; height: 66px;
    background: var(--pink);
    border: 3px solid var(--ink);
    display: flex; align-items: center; justify-content: center;
    font-family: "Russo One", sans-serif;
    font-size: 26px;
    color: var(--white);
  }
  .venue {
    position: absolute;
    left: 0; width: 720px; top: 930px;
    text-align: center;
    font-family: "Oswald", sans-serif;
    font-weight: 600;
    font-size: 32px;
    color: var(--ink);
  }
  .stars {
    position: absolute;
    left: 180px; top: 982px;
    width: 360px; height: 20px;
  }
  .call-banner {
    position: absolute;
    left: 30px; top: 1012px;
    width: 660px; height: 56px;
    background: linear-gradient(180deg, var(--pink-light), var(--pink) 60%, var(--pink-deep));
    clip-path: polygon(0 0, 100% 0, 97% 50%, 100% 100%, 0 100%, 3% 50%);
    display: flex; align-items: center; justify-content: center;
    font-family: "Russo One", sans-serif;
    font-size: 27px;
    letter-spacing: 1px;
    color: var(--white);
  }
  .contact-row {
    position: absolute;
    left: 40px; right: 40px; top: 1100px;
    display: flex; justify-content: space-between;
    font-family: "Russo One", sans-serif;
    font-size: 17px;
    color: var(--ink);
  }
</style>
</head>
<body>
  <main class="poster">
    <section class="card">
      <div class="dancer-photo" role="img" aria-label="Photo of a dancer in a green hooded top and jeans mid-move, with blue and green light bursts behind"></div>

      <h1 class="brand-name">KITO</h1>
      <p class="ensemble">DANCE ENSEMBLE</p>

      <div class="presents-band"><span>PRESENTS</span></div>
      <h2 class="title-band">KITO RISE AND GLOW DANCE FITNESS</h2>

      <p class="class-list">
        <span class="accent">AFRICAN DANCE</span>
        <span>MODERN SAMTIDSDANS</span>
        <span class="accent">YOGA/RITMOFLEX</span>
        <span>HIP HOP</span>
      </p>

      <p class="massage-box">MASSAGE AND REPERTOIRE CLASSES.</p>

      <p class="venue">VENUE:VETLEFJORD KULTURHUS</p>

      <svg class="stars" viewBox="0 0 360 20" aria-hidden="true">
        <defs>
          <polygon id="star" points="9,1 11.2,7 17.5,7 12.4,10.8 14.3,17 9,13.2 3.7,17 5.6,10.8 0.5,7 6.8,7" fill="#2b2f33"/>
        </defs>
        <use href="#star" x="0"/><use href="#star" x="18"/><use href="#star" x="36"/><use href="#star" x="54"/>
        <use href="#star" x="72"/><use href="#star" x="90"/><use href="#star" x="108"/><use href="#star" x="126"/>
        <use href="#star" x="144"/><use href="#star" x="162"/><use href="#star" x="180"/><use href="#star" x="198"/>
        <use href="#star" x="216"/><use href="#star" x="234"/><use href="#star" x="252"/><use href="#star" x="270"/>
        <use href="#star" x="288"/><use href="#star" x="306"/><use href="#star" x="324"/><use href="#star" x="342"/>
      </svg>

      <p class="call-banner">CALL 47351208 TO REGISTER/TEXT</p>

      <footer class="contact-row">
        <span>KITOARTS@KITOMAIL.EXAMPLE</span>
        <span>WWW.KITOARTS-EXAMPLE.ORG</span>
      </footer>
    </section>
  </main>
</body>
</html>
```